BRV Company Introduction Presentation for Industrial Electronics and Automation

We are established since 2011 and we have 50 employees. We have two divisions in our company in Industrial Electronics Repair and Automation Solutions. We would like to make a presentation for those two sectors in our company.

BRV COMPANY provides Industrial Electronics Repairs and Supplies as well as Automation Solutions.
Industrial Electronics: We repair and supply all kind of Industrial Electronic equipment including: PLCs, Drives, Servo Drives, Invertor, HMIs, Controllers .. Etc.
Automation Solutions: Provide Automation Solutions & Services.

We have several presentations attached for your guideline and you can use the material and wording in needed.
We are present in 3 countries: Kuwait, Saudi, UAE with 5 offices. I have attached some material that can help in the presentation.
Our customers:
Factories: F&B, Steel, Packing, Paper, Chemical, Glass
Services Companies: O&M, Transport, Marine
Electricity – Water – Wastewater: DOH, NAR
Oil & Gas (Government & Private: GZLT, Vorba, PMA, HRB
Building Management Systems: Malls, Commercial Buildings, Stadium

What items do we repair & Supply?
Power Supplies, Secondary DC Supplies, Processor Cards, Memory Cards, Interface Modules, Analog I/O Cards, Digital I/O Cards, Communication Cards, Remote I/O, Distribution Panel, Program Loaders, PCB (Boards).
Operation Panels, Servo Drives, Servo Motors, Axis cards, Processor Cards, Memory Cards.
All Servo Drives & Motors, Transducers, Interface Cards.
Wire Feeders, Weld Timers.
Industrial Monitors, Message/Status Display, Operator Interfaces .
Robot Arms

What are the added values of brv?
QFP - QUALITY / Fast / Price

Target Market(s)

Industrial Factories, Energy, Water, Wastewater and Oil & Gas.

Colors
86cae7
0692cd

Requirements
Must have
• - Vission, mission, goal
- Our journey
- services
- clients (Kuwait & Saudi)
- Major brands,
- facility
- certification
- automation projects
- contact details for 3 countries
Nice to have
• other things
Should not have
• nothing in mind

```html
<!DOCTYPE html>
<html lang="en">
<head>
<meta charset="utf-8">
<title>BRV Company Introduction Presentation</title>
<link rel="stylesheet" href="https://fonts.googleapis.com/css2?family=Montserrat:wght@400;500;600;700&display=swap">
<style>
:root{
  --blue:#0692cd;
  --blue-deep:#0a6fa8;
  --blue-light:#86cae7;
  --blue-pale:#d8eef8;
  --ink:#222a33;
  --white:#ffffff;
  --stage-top:#c7cad1;
  --stage-bottom:#e6e7ea;
  --page:#d5d4d7;
}
*{box-sizing:border-box;margin:0;padding:0}
html,body{width:1200px;height:2190px;overflow:hidden}
body{font-family:'Montserrat',sans-serif;color:var(--ink);background:var(--page);position:relative}
.stage{position:absolute;left:0;top:0;width:1200px;height:790px;background:linear-gradient(180deg,var(--stage-top),var(--stage-bottom) 70%,var(--page))}
.brand-hero{position:absolute;left:850px;top:160px;display:flex;align-items:center;gap:12px;font-weight:700;font-size:52px;color:var(--blue);letter-spacing:2px}
.brand-hero .dot,.logo .dot{border-radius:50%;background:var(--blue)}
.brand-hero .dot{width:40px;height:40px}
.hero-slide{transform:scale(1.15);transform-origin:0 0}

.slide{position:absolute;width:563px;height:316px;background:var(--white);overflow:hidden}
.logo{position:absolute;display:flex;align-items:center;gap:6px;font-weight:700;color:var(--blue)}
.logo.large{left:42px;top:22px;font-size:28px;letter-spacing:1px}
.logo.large .dot{width:22px;height:22px}
.logo.small{left:18px;top:278px;font-size:13px;background:var(--white);padding:0 4px}
.logo.small .dot{width:11px;height:11px}

.band{position:absolute;left:0;width:100%;background:linear-gradient(120deg,var(--blue-deep),var(--blue) 55%,#1f7fb8)}
.title-slide .band,.contact-slide .band{top:78px;height:220px}
.copyright{position:absolute;left:0;width:100%;top:301px;text-align:center;font-size:6px;color:#333}
.title{position:absolute;left:40px;top:112px;color:var(--white);font-weight:700;font-size:29px;line-height:31px}
.subtitle{position:absolute;left:40px;top:190px;color:var(--white);font-size:16px;line-height:18px}
.date{position:absolute;left:40px;top:248px;color:var(--white);font-size:8px}
.division{position:absolute;top:60px;width:50px;height:50px;border-radius:50%;background:var(--blue);border:3px solid var(--white);display:flex;align-items:center;justify-content:center}
.division-label{position:absolute;top:101px;width:64px;text-align:center;font-size:4px;letter-spacing:.2px;color:var(--white);font-weight:600}
.pill{position:absolute;top:56px;width:54px;height:132px;border-radius:27px;border:3px solid var(--white)}

.footer-bar{position:absolute;left:0;top:283px;width:100%;height:9px;background:var(--blue-light);color:var(--white);font-size:5.5px;text-align:right;padding-right:16px;line-height:9px}

.photo{position:absolute}
.heading{position:absolute;font-size:21px;font-weight:500;color:var(--ink)}
.heading b{color:var(--blue);font-weight:700}
.body{position:absolute;font-size:9px;line-height:10px;color:var(--ink)}
.body p+p{margin-top:5px}

.journey-track{position:absolute;left:0;top:112px;width:100%;height:106px;background:linear-gradient(180deg,var(--blue-pale),var(--blue-light) 50%,var(--blue-pale))}

.vision-slide .band{top:0;height:130px}
.vision-title{position:absolute;top:30px;width:100%;text-align:center;font-size:20px;color:var(--white)}
.vision-title b{font-weight:700}
.pillar{position:absolute;top:85px;width:150px;text-align:center}
.pillar .pic{height:87px;border-radius:10px 10px 0 0;border:2px solid var(--white)}
.pillar h3{margin-top:8px;font-size:14px;font-weight:500;color:var(--blue)}
.pillar p{margin-top:5px;font-size:8.5px;line-height:10px}

.service-label{position:absolute;font-size:10.5px;line-height:11px;color:var(--ink)}
.services-center{position:absolute;left:0;width:100%;top:178px;text-align:center;font-size:21px;line-height:22px;font-weight:500}
.services-center b{font-weight:700}

.contact-title{position:absolute;top:122px;width:100%;text-align:center;color:var(--white);font-size:20px;font-weight:500}
.office{position:absolute;top:170px;width:165px;height:80px;border-radius:10px;background:rgba(255,255,255,.14);padding:14px 16px;color:var(--white)}
.office h4{font-size:11px;font-weight:500;margin-bottom:8px}
.office div{display:flex;align-items:center;gap:8px;font-size:7.5px;margin-top:5px}
.office svg{width:9px;height:9px;flex:none}
</style>
</head>
<body>

<section class="stage">
  <div class="brand-hero"><span class="dot"></span>BRV</div>

  <article class="slide title-slide hero-slide" style="left:150px;top:200px">
    <div class="logo large"><span class="dot"></span>BRV</div>
    <div class="band" role="img" aria-label="Blue technology background with digital world map and robotic arm"></div>
    <div class="division" style="left:345px"><svg width="22" height="22" viewBox="0 0 22 22" fill="none" stroke="#fff" stroke-width="1.6"><rect x="6" y="6" width="10" height="10"/><path d="M9 2v4M13 2v4M9 16v4M13 16v4M2 9h4M2 13h4M16 9h4M16 13h4"/></svg></div>
    <div class="division" style="left:410px"><svg width="22" height="22" viewBox="0 0 22 22" fill="none" stroke="#fff" stroke-width="1.6"><path d="M4 19h10M8 19v-6l5-5M13 8l4 3M7 6a2 2 0 1 0 0.1 0"/></svg></div>
    <div class="division" style="left:475px"><svg width="22" height="22" viewBox="0 0 22 22" fill="none" stroke="#fff" stroke-width="1.6"><circle cx="11" cy="11" r="8"/><path d="M3 12h4l2-5 3 9 2-4h5"/></svg></div>
    <div class="title">Presentation Title<br>Goes Here!</div>
    <div class="subtitle">Subtitle of Presentation<br>Goes Here!</div>
    <div class="date">Friday, April 16, 2021</div>
    <div class="copyright">© Copyright BRV Company</div>
  </article>
</section>

<article class="slide title-slide" style="left:28px;top:810px">
  <div class="logo large"><span class="dot"></span>BRV</div>
  <div class="band" role="img" aria-label="Blue technology background with digital world map and robotic arm"></div>
  <div class="division" style="left:345px"><svg width="22" height="22" viewBox="0 0 22 22" fill="none" stroke="#fff" stroke-width="1.6"><rect x="6" y="6" width="10" height="10"/><path d="M9 2v4M13 2v4M9 16v4M13 16v4M2 9h4M2 13h4M16 9h4M16 13h4"/></svg></div>
  <div class="division" style="left:408px"><svg width="22" height="22" viewBox="0 0 22 22" fill="none" stroke="#fff" stroke-width="1.6"><path d="M4 19h10M8 19v-6l5-5M13 8l4 3M7 6a2 2 0 1 0 0.1 0"/></svg></div>
  <div class="division" style="left:471px"><svg width="22" height="22" viewBox="0 0 22 22" fill="none" stroke="#fff" stroke-width="1.6"><circle cx="11" cy="11" r="8"/><path d="M3 12h4l2-5 3 9 2-4h5"/></svg></div>
  <div class="division-label" style="left:338px">ELECTRONIC</div>
  <div class="division-label" style="left:401px">AUTOMATION</div>
  <div class="division-label" style="left:464px">BIOMEDICAL</div>
  <div class="title">Presentation Title<br>Goes Here!</div>
  <div class="subtitle">Subtitle of Presentation<br>Goes Here!</div>
  <div class="date">Friday, April 16, 2021</div>
  <div class="copyright">© Copyright BRV Company</div>
</article>

<article class="slide title-slide" style="left:609px;top:810px">
  <div class="logo large"><span class="dot"></span>BRV</div>
  <div class="band" role="img" aria-label="Blue technology background with digital world map and robotic arm"></div>
  <div class="pill" style="left:338px;background:linear-gradient(160deg,#2a6f9e,#123c5c)" role="img" aria-label="Photo of an electronic circuit board"></div>
  <div class="pill" style="left:401px;background:linear-gradient(160deg,#d9e6ee,#7d95a8)" role="img" aria-label="Photo of an industrial bearing and automation part"></div>
  <div class="pill" style="left:464px;background:linear-gradient(160deg,#e8f1f7,#8fb2c9)" role="img" aria-label="Photo of a biomedical equipment room"></div>
  <div class="title">Presentation Title<br>Goes Here!</div>
  <div class="subtitle">Subtitle of Presentation<br>Goes Here!</div>
  <div class="date">Friday, April 16, 2021</div>
  <div class="copyright">© Copyright BRV Company</div>
</article>

<article class="slide about-slide" style="left:28px;top:1145px">
  <div class="photo" style="left:27px;top:0;width:247px;height:254px;background:radial-gradient(circle at 60% 40%,#3aa4e0,#0b3f78 60%,#061b3a)" role="img" aria-label="Digital globe with glowing network connections"></div>
  <div class="heading" style="left:300px;top:72px">About <b>BRV</b></div>
  <div class="body" style="left:300px;top:112px;width:235px">
    <p>BRV is a Gulf Enterprise Fund supported company, till date provided services to 30,000 Industrial electronic equipment's and supported 2,000 clients in Kuwait and Saudi.</p>
    <p>We are established since 2011 and we have 50 employees. We have two divisions in our company in Industrial Electronics Repair and Automation Solutions. We would like to make a presentation for those two sectors in our company.</p>
  </div>
  <div class="footer-bar">© Copyright BRV Company &nbsp;|&nbsp; 3</div>
  <div class="logo small"><span class="dot"></span>BRV</div>
</article>

<article class="slide journey-slide" style="left:609px;top:1145px">
  <div class="heading" style="left:0;width:100%;text-align:center;top:22px">Our <b>Journey</b></div>
  <div class="journey-track" role="img" aria-label="Winding road illustration running through the timeline years"></div>
  <svg width="563" height="316" viewBox="0 0 563 316" style="position:absolute;left:0;top:0" font-family="Montserrat, sans-serif">
    <g fill="#0692cd" font-size="10" font-weight="500" text-anchor="middle">
      <text x="65" y="185">2012</text><text x="127" y="143">2013</text>
      <text x="189" y="185">2014</text><text x="251" y="143">2015</text>
      <text x="313" y="185">2017</text><text x="375" y="143">2018</text>
      <text x="437" y="185">2019</text><text x="499" y="143">2020</text>
    </g>
    <g stroke="#0692cd" stroke-width="1.5">
      <path d="M65 213v5M189 213v5M313 213v5M437 213v5M127 104v5M251 104v5M375 104v5M499 104v5"/>
    </g>
    <g fill="#222a33" font-size="7.5" text-anchor="middle">
      <text x="127" y="62">Automation</text><text x="127" y="71">Solutions</text><text x="127" y="80">Field</text><text x="127" y="89">Maintenance -</text><text x="127" y="98">AMC</text>
      <text x="251" y="80">Dammam</text><text x="251" y="89">(KSA)</text><text x="251" y="98">Established</text>
      <text x="375" y="89">Smart Control</text><text x="375" y="98">Solutions</text>
      <text x="499" y="98">Dubai (UAE)</text>
      <text x="65" y="228">Industrial</text><text x="65" y="237">Electronics</text><text x="65" y="246">Services</text>
      <text x="189" y="228">Riyadh (KSA)</text><text x="189" y="237">Established</text>
      <text x="313" y="228">Energy</text><text x="313" y="237">Monitoring</text><text x="313" y="246">Solutions</text>
      <text x="437" y="228">Jeddah (KSA)</text><text x="437" y="237">Established</text>
    </g>
  </svg>
  <div class="footer-bar">© Copyright BRV Company &nbsp;|&nbsp; 4</div>
  <div class="logo small"><span class="dot"></span>BRV</div>
</article>

<article class="slide vision-slide" style="left:28px;top:1480px">
  <div class="band" role="img" aria-label="Blue technology background"></div>
  <div class="vision-title">Our <b>Vision, Mission and Goal</b></div>
  <div class="pillar" style="left:40px">
    <div class="pic" style="background:linear-gradient(180deg,#f3c27a,#b9622c)" role="img" aria-label="Person looking through office windows at sunset"></div>
    <h3>Our Vision</h3>
    <p>To become the leading solution provider in GCC for Industrial Electronic Services, Automation and Energy Efficiency Services</p>
  </div>
  <div class="pillar" style="left:207px">
    <div class="pic" style="background:linear-gradient(180deg,#9aa3ab,#e3d9c8)" role="img" aria-label="Hand placing a dart on a target beside a laptop"></div>
    <h3>Our Mission</h3>
    <p>Develop new solutions to mitigate market challenges in Industrial Sector</p>
  </div>
  <div class="pillar" style="left:375px">
    <div class="pic" style="background:linear-gradient(180deg,#e79a3c,#5a2c14)" role="img" aria-label="Person with flag on a mountain top at sunrise"></div>
    <h3>Our Goal</h3>
    <p>Offer A One Stop Shop - cost effective solutions for all industrial sector in Controls, Automation and Energy Efficiency Field</p>
  </div>
  <div class="footer-bar">© Copyright BRV Company &nbsp;|&nbsp; 5</div>
  <div class="logo small"><span class="dot"></span>BRV</div>
</article>

<article class="slide services-slide" style="left:609px;top:1480px">
  <svg width="563" height="316" viewBox="0 0 563 316" style="position:absolute;left:0;top:0">
    <circle cx="282" cy="212" r="135" fill="none" stroke="#f1f3f5" stroke-width="10"/>
    <circle cx="282" cy="103" r="25" fill="#86cae7"/>
    <circle cx="185" cy="143" r="25" fill="#0692cd"/>
    <circle cx="378" cy="143" r="25" fill="#0692cd"/>
    <circle cx="148" cy="230" r="25" fill="#86cae7"/>
    <circle cx="415" cy="230" r="25" fill="#86cae7"/>
    <g fill="none" stroke="#fff" stroke-width="1.8">
      <circle cx="277" cy="105" r="5"/><circle cx="288" cy="100" r="4"/>
      <path d="M178 152l3-8 9-9 4 4-9 9zM178 152h14"/>
      <path d="M371 139h5l9-6v20l-9-6h-5z"/>
      <path d="M148 238v-3M144 224a5 5 0 1 1 8 0c-1 2-2 3-2 8h-4c0-5-1-6-2-8z"/>
      <path d="M406 221l18 18M424 221l-18 18"/>
    </g>
  </svg>
  <div class="service-label" style="left:0;width:100%;text-align:center;top:30px">Industrial<br>Annual<br>Maintenance</div>
  <div class="service-label" style="left:80px;width:75px;text-align:right;top:133px">Industrial<br>Automation</div>
  <div class="service-label" style="left:418px;top:133px">Emergency<br>Services</div>
  <div class="service-label" style="left:50px;width:68px;text-align:right;top:219px">Energy<br>Efficiency<br>Services</div>
  <div class="service-label" style="left:455px;top:222px">Industrial<br>Repair</div>
  <div class="services-center">Our<br><b>Services</b></div>
  <div class="footer-bar">© Copyright BRV Company &nbsp;|&nbsp; 6</div>
  <div class="logo small"><span class="dot"></span>BRV</div>
</article>

<article class="slide contact-slide" style="left:319px;top:1815px">
  <div class="logo large"><span class="dot"></span>BRV</div>
  <div class="band" role="img" aria-label="Blue technology background with digital world map"></div>
  <div class="contact-title">Contact Us</div>
  <div class="office" style="left:29px">
    <h4>KUWAIT</h4>
    <div><svg viewBox="0 0 10 10" fill="#fff"><path d="M2 0l2 2-1 2 3 3 2-1 2 2-2 2C4 10 0 6 0 2z"/></svg>+965 2000 1100</div>
    <div><svg viewBox="0 0 10 10" fill="none" stroke="#fff" stroke-width="1.3"><circle cx="5" cy="5" r="2"/><path d="M7 3v3c0 1 2 1 2-1a4 4 0 1 0-2 3.5"/></svg>info@brv-me.com</div>
  </div>
  <div class="office" style="left:199px">
    <h4>SAUDI ARABIA</h4>
    <div><svg viewBox="0 0 10 10" fill="#fff"><path d="M2 0l2 2-1 2 3 3 2-1 2 2-2 2C4 10 0 6 0 2z"/></svg>+966 11 0000 222</div>
    <div><svg viewBox="0 0 10 10" fill="none" stroke="#fff" stroke-width="1.3"><circle cx="5" cy="5" r="2"/><path d="M7 3v3c0 1 2 1 2-1a4 4 0 1 0-2 3.5"/></svg>info-sa@brv-me.com</div>
  </div>
  <div class="office" style="left:369px">
    <h4>UAE</h4>
    <div><svg viewBox="0 0 10 10" fill="#fff"><path d="M2 0l2 2-1 2 3 3 2-1 2 2-2 2C4 10 0 6 0 2z"/></svg>+971 50 0000 333</div>
    <div><svg viewBox="0 0 10 10" fill="none" stroke="#fff" stroke-width="1.3"><circle cx="5" cy="5" r="2"/><path d="M7 3v3c0 1 2 1 2-1a4 4 0 1 0-2 3.5"/></svg>info-uae@brv-</div>
  </div>
  <div class="copyright">© Copyright BRV Company</div>
</article>

</body>
</html>
```